Title: Iron Lantern Sub: A quiet road through winter - Book cover

I need a complete book cover, front, spine, and back.

Religions Book

This book is more about the Title so it should be strong and serious.

Like the color Deep Red and black, blue. Deep purple
Avoid greens, orange, yellows.

Maybe a picture of a strong hand on the Bible. OR someone yelling.

If any pictures are used they must be 100% royalty free with proof or a buyout of image.

I have attached a couple of designs that the client likes. Just as a reference. The exception they DIDN'T like the pictures in the book cover.

Please ask any questions to clarify.

Please see the file I just uploaded called 'Book Cover samples.png" The clients likes the Title: Salt and Ember" the best. Please create a design something closer to this. The like how the title jumps off the page with a 2D look.

Again the Title must standout, and any use of images must be a secondary to the design.

I am happy with we the designs that have been submitted so far.

I hope this helps you get closer.

Thank you

First of all I want to thank you for all of your designs. At the beginning the client thought he would like a picture that represented the title. But after looking at all of the designs. He has now decided NOT to have any pictures.

Here is what he wants

1. BOLD Font (San Serif only) no fancy versions for the Title "IRON LANTERN" in uppercase. The title font should have some dimension to it to appear 2D or 3D looks. Shiny look. It needs to looks like it jumping off the page.

2. The subtitle right below the title in San Serif font)

3. Background solid color either black, dark red, or dark blue. The background can be slightly textured or gradation fill, etc.

4. The cover must have a strong and bold statement.

Thank you again.

Please use this photo on the back cover.

Thank you

• A picture that over powers the Title.

```html
<!DOCTYPE html>
<html lang="en">
<head>
<meta charset="utf-8">
<title>Iron Lantern – Book Cover</title>
<link href="https://fonts.googleapis.com/css2?family=Bebas+Neue&family=Oswald:wght@600;700&family=Roboto+Condensed:wght@400&display=swap" rel="stylesheet">
<style>
  :root{
    --wine-deep:#3e0a16;
    --wine:#5c1424;
    --wine-light:#74202f;
    --rule-white:#e9dcdc;
    --gold-light:#fbeacb;
    --gold:#e7c58c;
    --gold-dark:#b88a4a;
    --ink-red:#6e0c0f;
    --paper:#ffffff;
  }
  *{box-sizing:border-box;margin:0;padding:0}
  html,body{width:1200px;height:847px;overflow:hidden;background:var(--wine-deep)}
  .cover{
    position:relative;width:1200px;height:847px;overflow:hidden;
    background:
      radial-gradient(ellipse at 25% 35%, var(--wine-light) 0%, transparent 60%),
      radial-gradient(ellipse at 78% 30%, var(--wine-light) 0%, transparent 60%),
      linear-gradient(180deg, var(--wine) 0%, var(--wine-deep) 100%);
  }
  .spine-edge{position:absolute;top:0;width:1px;height:847px;background:var(--rule-white);opacity:.85}
  .spine-edge--left{left:543px}
  .spine-edge--right{left:657px}

  /* back cover */
  .back-title{position:absolute;left:135px;top:38px;width:256px;text-align:center;
    font-family:'Bebas Neue',sans-serif;color:var(--paper);text-shadow:0 3px 6px rgba(0,0,0,.45)}
  .back-title__top{display:block;font-size:186px;line-height:170px}
  .back-title__rule{display:block;height:7px;margin:4px 0 8px;background:linear-gradient(90deg,var(--gold-dark),var(--gold-light),var(--gold))}
  .back-title__bottom{display:block;font-size:94px;line-height:86px}

  .bio{position:absolute;left:46px;top:367px;width:451px;
    font-family:'Roboto Condensed',sans-serif;font-size:14px;line-height:20.4px;color:var(--paper);text-align:justify}
  .bio__photo{float:left;width:189px;height:210px;margin:0 10px 4px 0;
    background:radial-gradient(ellipse at 50% 40%,#d9a98d 0%,#b98066 35%,#f3f3f3 70%)}
  .site-band{position:absolute;left:50px;top:742px;width:442px;height:43px;
    background:linear-gradient(90deg,var(--gold-dark),var(--gold-light) 45%,var(--gold) 100%);
    display:flex;align-items:center;justify-content:center;
    font-family:'Oswald',sans-serif;font-weight:700;font-size:24px;letter-spacing:2px;color:var(--ink-red)}

  /* spine */
  .spine-title{position:absolute;left:562px;top:140px;height:370px;writing-mode:vertical-rl;
    font-family:'Bebas Neue',sans-serif;font-size:70px;line-height:76px;color:var(--paper);
    display:flex;align-items:center;justify-content:center;white-space:nowrap}
  .spine-rule{position:absolute;left:639px;top:145px;width:4px;height:362px;
    background:linear-gradient(180deg,var(--gold-light),var(--gold-dark))}
  .spine-author{position:absolute;left:576px;top:594px;height:228px;writing-mode:vertical-rl;
    font-family:'Oswald',sans-serif;font-weight:700;font-size:27px;line-height:36px;color:var(--paper);
    display:flex;align-items:center;justify-content:center;white-space:nowrap}

  /* front cover */
  .front-title{position:absolute;left:737px;top:66px;width:372px;text-align:center;font-family:'Bebas Neue',sans-serif}
  .front-title__word{display:block;
    background:linear-gradient(180deg,var(--gold-light) 0%,var(--gold) 45%,#f6dcae 55%,var(--gold-dark) 100%);
    -webkit-background-clip:text;background-clip:text;color:transparent;
    filter:drop-shadow(0 0 2px #c9505e) drop-shadow(0 6px 8px rgba(0,0,0,.55))}
  .front-title__word--top{font-size:262px;line-height:244px}
  .front-title__rule{display:block;height:13px;margin:6px 0 10px;
    background:linear-gradient(90deg,var(--gold-dark),var(--gold-light) 50%,var(--gold));
    box-shadow:0 3px 6px rgba(0,0,0,.5)}
  .front-title__word--bottom{font-size:134px;line-height:118px}
  .front-subtitle{position:absolute;left:700px;top:466px;width:446px;text-align:center;
    font-family:'Bebas Neue',sans-serif;font-size:40px;line-height:44px;color:var(--paper);
    text-shadow:0 2px 4px rgba(0,0,0,.5)}
  .author-band{position:absolute;left:657px;top:688px;width:543px;height:87px;
    background:linear-gradient(90deg,var(--gold-dark),var(--gold-light) 40%,var(--gold) 75%,var(--gold-dark));
    box-shadow:0 4px 8px rgba(0,0,0,.45);
    display:flex;align-items:center;justify-content:center;
    font-family:'Oswald',sans-serif;font-weight:700;font-size:46px;color:var(--ink-red)}
</style>
</head>
<body>
<main class="cover">
  <section class="back">
    <h2 class="back-title">
      <span class="back-title__top">IRON</span>
      <span class="back-title__rule"></span>
      <span class="back-title__bottom">LANTERN</span>
    </h2>
    <div class="bio">
      <div class="bio__photo" role="img" aria-label="Author portrait photograph"></div>
      <p>Lorem ipsum dolor sit amet, consectetur adipiscing elit. In eget nibh eu nulla imperdiet feugiat. Cum sociis natoque penatibus et magnis dis parturient montes, nascetur ridiculus mus. Sed in ante consectetur sem feugiat eleifend ac vel enim. Fusce quis est in nisi pretium facilisis. Etiam adipiscing interdum libero, aliquam aliquet orci cursus quis. Aliquam lobortis lacus quis purus tempor pretium. Aliquam ut placerat dui. Integer dictum risus dui, sit amet consequat nunc blandit ac. Aenean porttitor eros at felis ornare feugiat. Aenean sit amet nulla sem. Proin sem neque, imperdiet aliquet pulvinar et, hendrerit nec augue. Interdum et malesuada fames ac ante ipsum primis in faucibus.</p>
    </div>
    <div class="site-band">WWW.MARCUSHALLORAN.COM</div>
  </section>

  <div class="spine-edge spine-edge--left"></div>
  <section class="spine">
    <div class="spine-title">IRON LANTERN</div>
    <div class="spine-rule"></div>
    <div class="spine-author">MARCUS HALLORAN</div>
  </section>
  <div class="spine-edge spine-edge--right"></div>

  <section class="front">
    <h1 class="front-title">
      <span class="front-title__word front-title__word--top">IRON</span>
      <span class="front-title__rule"></span>
      <span class="front-title__word front-title__word--bottom">LANTERN</span>
    </h1>
    <p class="front-subtitle">A QUIET ROAD THROUGH WINTER</p>
    <div class="author-band">MARCUS HALLORAN</div>
  </section>
</main>
</body>
</html>
```